Envelope Design Project

I will need two envelopes to be designed:-

DL size
C4 size

Please see uploaded documents for Design specs:

1) Design specs provided by printer (doc called DL Envelope Specs)
2) Design specs to comply with Kestrel Mailways requirements (doc called Kestrel Mailways Envelope Design Requirements)

Please adhere to the above for final design. Many thanks.

Target Market(s)

Real Estate Agents, Strata Managers, Builders, Architects, Business Owners

Industry/Entity Type

Printer

Requirements
Must have
• In top left corner
- Logo
- Return address - Suite 5, 19 Wattlebark Rd, Marrowick, NSW 2417

```html
<!DOCTYPE html>
<html lang="en">
<head>
<meta charset="utf-8">
<title>Zennoq Asbestos &amp; Safety – DL Envelope</title>
<link href="https://fonts.googleapis.com/css2?family=Didact+Gothic&display=swap" rel="stylesheet">
<style>
  :root {
    --navy: #1f2a52;
    --green: #8bbd3f;
    --ink: #2b2b2b;
    --paper: #ffffff;
    --backdrop: #e6e7e9;
  }
  * { margin: 0; padding: 0; box-sizing: border-box; }
  html, body {
    width: 1200px;
    height: 900px;
    overflow: hidden;
    background: var(--backdrop);
  }
  .canvas {
    position: relative;
    width: 1200px;
    height: 900px;
  }
  .envelope {
    position: absolute;
    left: 143px;
    top: 221px;
    width: 915px;
    height: 458px;
    background: var(--paper);
    font-family: "Didact Gothic", "Century Gothic", sans-serif;
    box-shadow: 0 2px 10px rgba(0,0,0,0.12);
    overflow: hidden;
  }
  .brand {
    position: absolute;
    left: 62px;
    top: 76px;
    display: flex;
    align-items: center;
    gap: 10px;
    height: 60px;
  }
  .brand-square {
    width: 40px;
    height: 40px;
    background: var(--navy);
  }
  .brand-name {
    font-size: 52px;
    line-height: 1;
    color: var(--green);
    letter-spacing: -1px;
  }
  .brand-descriptor {
    position: absolute;
    left: 68px;
    top: 146px;
    font-size: 19px;
    line-height: 22px;
    color: var(--navy);
    letter-spacing: 0.2px;
  }
  .return-address {
    position: absolute;
    left: 68px;
    top: 176px;
    font-size: 14px;
    line-height: 18px;
    color: var(--ink);
    font-style: normal;
  }
  .footer-bands {
    position: absolute;
    left: 0;
    bottom: 0;
  }
</style>
</head>
<body>
<div class="canvas">
  <section class="envelope">
    <div class="brand">
      <span class="brand-square"></span>
      <span class="brand-name">Zennoq</span>
    </div>
    <div class="brand-descriptor">ASBESTOS &amp; SAFETY</div>
    <address class="return-address">
      Suite 5, 19 Wattlebark Rd<br>
      Marrowick, NSW 2417
    </address>
    <svg class="footer-bands" width="915" height="42" viewBox="0 0 915 42" aria-hidden="true">
      <polygon points="0,12 330,12 316,42 0,42" fill="var(--navy)"/>
      <polygon points="348,0 915,0 915,42 320,42" fill="var(--green)"/>
    </svg>
  </section>
</div>
</body>
</html>
```